Priority Goals poster for school year

We are an elementary school and the past two years have had you help us to design a "poster" that illustrates our goal of the coming year. I am attaching our last year's one, along with some photos of our (ver rough) thinking for next years. The priority goal at top remains the same. Can't wait to see your genius ideas! :)

Target Market(s)

Staff of an elementary school and parents to some (informative) extent as well.

Colors
296eb1
6094c6
fbed22
fbee3f

Requirements
Must have
• items from the white board picture we have attached

```html
<!DOCTYPE html>
<html lang="en">
<head>
<meta charset="utf-8">
<title>2021-22 Priority Goals – Cedar Ridge Elementary School</title>
<link href="https://fonts.googleapis.com/css2?family=Montserrat:wght@700;800&family=Varela+Round&display=swap" rel="stylesheet">
<style>
  :root {
    --navy: #2b3b96;
    --wheel-dark: #2a4898;
    --wheel-light: #72a7d7;
    --gold: #ebc63a;
    --ring: #f0c419;
    --white: #ffffff;
    --mist: #eceef3;
  }
  * { margin: 0; padding: 0; box-sizing: border-box; }
  html, body { width: 863px; height: 1200px; overflow: hidden; background: var(--white); }
  .poster {
    position: relative; width: 863px; height: 1200px; overflow: hidden;
    background: var(--white); font-family: "Varela Round", sans-serif; color: var(--navy);
  }
  .abs { position: absolute; }

  .year {
    left: 175px; top: 8px; width: 300px; text-align: center;
    font-family: "Montserrat", sans-serif; font-weight: 800; font-size: 68px; line-height: 80px;
    color: var(--navy); letter-spacing: -1px;
  }
  .title-band { left: 0; top: 77px; width: 863px; height: 66px; background: var(--navy); }
  .title {
    left: 17px; top: 78px; font-family: "Montserrat", sans-serif; font-weight: 800;
    font-size: 58px; line-height: 64px; color: var(--white); letter-spacing: 0.5px;
  }
  .intro-band { left: 0; top: 143px; width: 863px; height: 65px; background: var(--gold); }
  .intro { left: 21px; top: 149px; font-size: 19.5px; line-height: 25px; color: var(--navy); }

  .backdrop {
    left: 0; top: 208px; width: 863px; height: 780px;
    background: linear-gradient(180deg, #f3f3f6 0%, var(--mist) 55%, #f5f5f8 100%);
  }

  .school-mark {
    left: 606px; top: 22px; width: 240px; height: 234px; z-index: 3;
    background: var(--white); border-radius: 0 0 12px 12px;
    display: flex; flex-direction: column; align-items: center; justify-content: flex-end;
    gap: 14px; padding-bottom: 8px;
  }
  .school-mark .dot { width: 110px; height: 110px; border-radius: 50%; background: var(--gold); }
  .school-mark .name {
    font-family: "Montserrat", sans-serif; font-weight: 800; color: var(--navy);
    text-align: center; white-space: nowrap;
  }
  .school-mark .name-main { display: block; font-size: 27px; line-height: 30px; }
  .school-mark .name-sub { display: block; font-size: 16px; line-height: 20px; letter-spacing: 0.5px; }

  .wheel { left: 47px; top: 223px; width: 766px; height: 766px; }

  .seg-text { font-size: 17.5px; line-height: 23px; color: var(--white); }
  .seg-text.on-gold { color: var(--navy); }
  .seg-text p + p { margin-top: 5px; }
  .tag { background: var(--navy); color: var(--white); padding: 0 3px; }
  .tag-light { background: var(--white); color: var(--navy); padding: 0 3px; }
  .bullets { list-style: none; font-size: 16.5px; line-height: 24px; }
  .bullets li::before { content: "●"; font-size: 11px; margin-right: 5px; vertical-align: 2px; }
  .strong { font-family: "Montserrat", sans-serif; font-weight: 700; font-size: 18px; line-height: 22px; }

  .promises {
    left: 0; top: 992px; width: 863px; text-align: center;
    font-family: "Montserrat", sans-serif; font-weight: 800; font-size: 53px; line-height: 60px; color: var(--navy);
  }
  .promises-sub {
    left: 0; top: 1053px; width: 863px; text-align: center;
    font-family: "Varela Round", sans-serif; font-size: 27px; line-height: 32px; color: var(--navy);
  }

  .footer-strip { left: 0; top: 1101px; width: 863px; height: 13px; background: var(--gold); }
  .footer { left: 0; top: 1114px; width: 863px; height: 86px; background: var(--navy); color: var(--white); }
  .address { left: 62px; top: 1128px; font-family: "Montserrat", sans-serif; font-weight: 700; font-size: 19px; line-height: 26px; color: var(--white); }
  .phone { left: 60px; top: 1159px; font-family: "Montserrat", sans-serif; font-weight: 700; font-size: 29px; line-height: 36px; color: var(--white); }
  .pin { left: 32px; top: 1130px; }
  .handset { left: 34px; top: 1168px; }
  .social-box { left: 594px; top: 1143px; width: 32px; height: 32px; border-radius: 7px; background: var(--white); }
  .handle { left: 634px; top: 1144px; font-size: 19px; line-height: 28px; color: var(--white); }
</style>
</head>
<body>
<main class="poster">
  <div class="abs year">2021-22</div>
  <div class="abs title-band"></div>
  <h1 class="abs title">PRIORITY GOALS</h1>
  <div class="abs intro-band"></div>
  <p class="abs intro">We will accelerate the academic &amp; Social/Emotional<br>Growth of the students we serve by:</p>

  <div class="abs backdrop" role="img" aria-label="Faint school mascot and chalkboard math sketches in the background"></div>

  <div class="abs school-mark">
    <span class="dot"></span>
    <span class="name"><span class="name-main">CEDAR RIDGE</span><span class="name-sub">ELEMENTARY SCHOOL</span></span>
  </div>

  <svg class="abs wheel" viewBox="-254 -254 508 508" aria-label="Priority goals wheel">
    <circle cx="0" cy="0" r="250" fill="var(--white)" stroke="var(--ring)" stroke-width="4"/>
    <g class="segments">
      <path d="M0,0 Q-88.7,-95.1 -12.3,-235.7 A236,236 0 0 1 157.9,-175.4 Q4.5,-129.9 0,0Z" fill="var(--wheel-dark)"/>
      <path d="M0,0 Q4.5,-129.9 157.9,-175.4 A236,236 0 0 1 235.7,-12.4 Q95.1,-88.7 0,0Z" fill="var(--gold)"/>
      <path d="M0,0 Q95.1,-88.7 235.7,-12.4 A236,236 0 0 1 175.4,157.9 Q129.9,4.5 0,0Z" fill="var(--wheel-dark)"/>
      <path d="M0,0 Q129.9,4.5 175.4,157.9 A236,236 0 0 1 12.4,235.7 Q88.7,95.1 0,0Z" fill="var(--gold)"/>
      <path d="M0,0 Q88.7,95.1 12.4,235.7 A236,236 0 0 1 -157.9,175.4 Q-4.5,129.9 0,0Z" fill="var(--wheel-light)"/>
      <path d="M0,0 Q-4.5,129.9 -157.9,175.4 A236,236 0 0 1 -235.7,12.4 Q-95.1,88.7 0,0Z" fill="var(--wheel-dark)"/>
      <path d="M0,0 Q-95.1,88.7 -235.7,12.4 A236,236 0 0 1 -175.4,-157.9 Q-129.9,-4.5 0,0Z" fill="var(--gold)"/>
      <path d="M0,0 Q-129.9,-4.5 -175.4,-157.9 A236,236 0 0 1 -12.3,-235.7 Q-88.7,-95.1 0,0Z" fill="var(--wheel-light)"/>
    </g>
    <rect x="-30" y="-128" width="60" height="72" rx="14" fill="var(--white)" opacity="0.9" role="img" aria-label="Graduate figure in a mortarboard cap"/>
    <path class="heart" d="M0,-42 C-25,-75 -90,-75 -90,-22 C-90,20 -40,55 0,88 C40,55 90,20 90,-22 C90,-75 25,-75 0,-42Z" fill="var(--white)" stroke="#dedfe3" stroke-width="4"/>
    <rect x="-58" y="-38" width="116" height="86" rx="10" fill="#e8ecf6" role="img" aria-label="Icons of a teacher with students, a connected team and a school building"/>
  </svg>

  <div class="abs seg-text" style="left:221px;top:346px;width:130px;">
    <p>Voices of <span class="tag">All</span></p>
    <p>Who are we?</p>
    <p>Where are we going?</p>
  </div>
  <div class="abs seg-text" style="left:410px;top:333px;">Broaden our Lead</div>
  <div class="abs seg-text on-gold" style="left:566px;top:432px;width:170px;">
    <p>Staff doing what they Love...</p>
    <p>Teaching kids for Proven Growth</p>
  </div>
  <div class="abs seg-text on-gold" style="left:118px;top:530px;width:160px;line-height:27px;">Small Measured<br>Step Towards<br>Larger Goal</div>
  <div class="abs seg-text" style="left:593px;top:572px;width:150px;">Communicate,<br>Communicate,<br>Communicate,</div>
  <ul class="abs bullets" style="left:615px;top:658px;color:var(--white);">
    <li><span class="tag-light">Expectations</span></li>
  </ul>
  <ul class="abs bullets" style="left:632px;top:684px;color:var(--white);"><li>Support</li></ul>
  <ul class="abs bullets" style="left:642px;top:709px;color:var(--white);"><li>For Clarity</li></ul>

  <div class="abs strong" style="left:492px;top:730px;color:var(--navy);">Build Value</div>
  <div class="abs strong" style="left:490px;top:753px;"><span class="tag-light">Partnership</span></div>
  <ul class="abs bullets" style="left:491px;top:778px;color:var(--navy);">
    <li>Correct</li><li>Celebrate</li><li>Strong, Predictable</li><li>Laugh,Have Fun</li>
  </ul>

  <div class="abs seg-text" style="left:129px;top:707px;width:190px;">Be intentional with each action- Focus</div>
  <div class="abs seg-text" style="left:276px;top:806px;width:200px;">
    <p style="padding-left:24px;"><span class="tag strong" style="color:var(--white);">Wellness</span></p>
    <p style="font-size:16px;line-height:22px;">Mental Health for every person in our school community</p>
  </div>

  <h2 class="abs promises">FOUNDATIONAL PROMISES</h2>
  <p class="abs promises-sub">( 4 YEARS STRONG, BETTER EVERYDAY )</p>

  <div class="abs footer-strip"></div>
  <div class="abs footer"></div>
  <svg class="abs pin" width="22" height="26" viewBox="0 0 22 26" aria-hidden="true">
    <path d="M11 1C5.5 1 2 5 2 10c0 6.5 9 15 9 15s9-8.5 9-15c0-5-3.5-9-9-9z" fill="none" stroke="var(--white)" stroke-width="2.5"/>
    <circle cx="11" cy="10" r="3.5" fill="var(--white)"/>
  </svg>
  <p class="abs address">1870 Birchwood Ave., Lakeview, WA 98100</p>
  <svg class="abs handset" width="18" height="22" viewBox="0 0 18 22" aria-hidden="true">
    <path d="M6 2 L9 7 L7 9 C8 12 10 15 12 16 L14 14 L17 18 L14 21 C7 19 2 11 3 4Z" fill="var(--white)"/>
  </svg>
  <p class="abs phone">555-013-2400</p>
  <span class="abs social-box"></span>
  <p class="abs handle">@cedarridgelearners</p>
</main>
</body>
</html>
```